GLSW Canberra Pty Ltd

Want something creative and that catches your eye. We are a traffic control companythat offers all aspects of traffic control from planning to roadworks.

Contact Information for Business Card

Dean Vorlick - Director
Ph: 0481 375 206
Email: dean@glsw.com.au
27 Marlow Binks ct Chisholm ACT 2905

```html
<!DOCTYPE html>
<html lang="en">
<head>
<meta charset="utf-8">
<title>GLSW Canberra – Business Card</title>
<link rel="stylesheet" href="https://fonts.googleapis.com/css2?family=Open+Sans:wght@400;600;700&display=swap">
<style>
  :root {
    --stage: #2b2b2b;
    --card-white: #f7f7f7;
    --ink: #1c1c1c;
    --ink-soft: #8a8a8a;
    --accent: #d9533b;
    --accent-light: #f0a08c;
    --road-green: #a9c48a;
    --road-green-light: #d3e2c0;
    --road-grey: #7a7a7a;
    --back-brown: #4a413d;
    --back-band: #cfcdcb;
    --back-text: #b9b2ad;
  }
  * { box-sizing: border-box; margin: 0; padding: 0; }
  html, body { width: 1200px; height: 1000px; overflow: hidden; }
  body {
    background: var(--stage);
    font-family: "Open Sans", Arial, sans-serif;
    position: relative;
  }
  .card {
    position: absolute;
    left: 250px;
    width: 700px;
    height: 428px;
    overflow: hidden;
    box-shadow: 0 10px 30px rgba(0,0,0,.45);
  }

  /* Front */
  .card-front { top: 50px; background: linear-gradient(135deg, #ffffff 0%, var(--card-white) 60%, #e9e9e9 100%); }
  .brand {
    position: absolute; left: 40px; top: 38px;
    display: flex; align-items: center; gap: 12px;
  }
  .brand-dot { width: 46px; height: 46px; border-radius: 50%; background: var(--accent); }
  .brand-name { font-size: 30px; font-weight: 700; color: var(--ink); letter-spacing: 1px; line-height: 1; }
  .brand-sub { display: block; font-size: 12px; font-weight: 700; color: var(--ink); letter-spacing: 3px; margin-top: 4px; }
  .holder { position: absolute; right: 36px; top: 30px; text-align: right; }
  .holder-name { font-size: 30px; font-weight: 700; color: var(--ink); line-height: 1.1; }
  .holder-role { font-size: 18px; color: var(--ink-soft); line-height: 1.1; }
  .feature-art {
    position: absolute; left: 468px; top: 112px; width: 300px; height: 300px;
  }
  .contact { position: absolute; left: 40px; bottom: 34px; font-size: 20px; line-height: 1.55; color: var(--ink); }
  .contact dt { display: inline; font-weight: 700; }
  .contact dd { display: inline; color: var(--ink-soft); }
  .contact .address { font-weight: 700; font-size: 21px; }

  /* Back */
  .card-back { top: 522px; background: var(--back-brown); }
  .back-band-top {
    position: absolute; left: 0; top: 0; width: 100%; height: 78px;
    background: linear-gradient(#e2e0de, var(--back-band));
    display: flex; align-items: center; justify-content: center; gap: 10px;
  }
  .back-band-bottom {
    position: absolute; left: 0; bottom: 0; width: 100%; height: 56px;
    background: linear-gradient(#b9b6b3, #a8a4a1);
  }
  .back-band-top .brand-dot { width: 34px; height: 34px; background: #7a7472; }
  .back-band-top .brand-name { font-size: 24px; color: #5b5553; }
  .services {
    position: absolute; left: 0; top: 92px; width: 100%;
    list-style: none; text-align: center;
    color: var(--back-text); font-size: 17px; line-height: 1.3;
  }
</style>
</head>
<body>
  <section class="card card-front">
    <div class="brand">
      <span class="brand-dot"></span>
      <span class="brand-name">GLSW<span class="brand-sub">CANBERRA</span></span>
    </div>
    <div class="holder">
      <div class="holder-name">Dean Vorlick</div>
      <div class="holder-role">Director</div>
    </div>
    <svg class="feature-art" viewBox="0 0 300 300" role="img" aria-label="Illustration of a winding road with a stop sign inside an octagon frame">
      <defs>
        <linearGradient id="frameFill" x1="0" y1="0" x2="0" y2="1">
          <stop offset="0" stop-color="var(--accent)"/>
          <stop offset="1" stop-color="var(--accent-light)"/>
        </linearGradient>
        <linearGradient id="sceneFill" x1="0" y1="0" x2="0.4" y2="1">
          <stop offset="0" stop-color="var(--road-green)"/>
          <stop offset="0.5" stop-color="var(--road-green-light)"/>
          <stop offset="1" stop-color="var(--road-grey)"/>
        </linearGradient>
      </defs>
      <polygon class="art-frame" points="88,0 212,0 300,88 300,212 212,300 88,300 0,212 0,88" fill="url(#frameFill)" opacity=".75"/>
      <polygon class="art-scene" points="92,10 208,10 290,92 290,208 208,290 92,290 10,208 10,92" fill="url(#sceneFill)" opacity=".85"/>
    </svg>
    <dl class="contact">
      <div><dt>Ph:</dt> <dd>0481 375 206</dd></div>
      <div><dt>Email:</dt> <dd>dean@glsw.com.au</dd></div>
      <div class="address">27 Marlow Binks ct Chisholm ACT 2905</div>
    </dl>
  </section>

  <section class="card card-back">
    <div class="back-band-top">
      <span class="brand-dot"></span>
      <span class="brand-name">GLSW</span>
    </div>
    <ul class="services">
      <li>Industrial Relation &amp; Employment Accredited for ACT</li>
      <li>Capital Grid Accredited</li>
      <li>Regional Power</li>
      <li>Emergency Response Vehicles</li>
      <li>24 Hour Services</li>
      <li>TTM Planning &amp; Design for ACT</li>
      <li>Traffic Management Planning and Design</li>
      <li>Traffic Engineering Consultants</li>
      <li>Traffic Control</li>
      <li>ACT Accredited</li>
      <li>Local Council Approval</li>
      <li>Local Council Consultants</li>
    </ul>
    <div class="back-band-bottom"></div>
  </section>
</body>
</html>
```